Quorvia medical teaching of the future

responsive website, onepager, for medical technology company. It has to look clean and high tech.

Look & feel
• Responsive
• Clean
• Combination icons + foto's
• Integration of a YouTube video

Landingpage items

• Header: picture + 'a video-based teaching platform for surgical procedures'
• About Deferred live medical teaching: Short description
• Features
o Video
o Teaching platform

• Benefits:
o More effective learning
o Faster sharing of knowledge & tecniques
o More cost effective

• References

• Products:
o Live (+link to more info)
o bTamo (+ link to more info)
o bTamo local (+link to more info)
o bTamo cloud (+ link to more info)

• Solutions:
o For medical device companies (+link to more info)
o Doctor and surgeons (+link to more info)
o Medical conferences (+link to more info)

Target Market(s)

medical device companies
surgeons and doctors
conference organisers

Industry/Entity Type

It Company

Number of Pages Required

1 page

Requirements
Must have
• Landingpage items
• • Header: picture + 'a video-based teaching platform for surgical procedures'
• • About Deferred live medical teaching: Short description
• • Features
• o Video
• o Teaching platform
• • Benefits:
• o More effective learning
• o Faster sharing of knowledge & tecniques
• o More cost effective
• • References
• • Products:
• o Live (+link to more info)
• o bTamo (+ link to more info)
• o bTamo local (+link to more info)
• o bTamo cloud (+ link to more info)
• • Solutions:
• o For medical device companies (+link to more info)
• o Doctor and surgeons (+link to more info)
• o Medical conferences (+link to more info)
Nice to have
• possibilty to show video

```html
<!DOCTYPE html>
<html lang="en">
<head>
<meta charset="utf-8">
<title>Quorvia – medical teaching of the future</title>
<link rel="stylesheet" href="https://fonts.googleapis.com/css2?family=Roboto:wght@300;400;500;700&family=Open+Sans:wght@400;600&display=swap">
<style>
:root{
  --teal:#4f9f96;
  --teal-dark:#3d857c;
  --red:#c4161c;
  --ink:#333;
  --muted:#777;
  --light:#f2f2f2;
  --dark:#1f1f1f;
  --white:#fff;
}
*{box-sizing:border-box;margin:0;padding:0}
html,body{width:1200px;height:4080px;overflow:hidden}
body{font-family:"Open Sans",Arial,sans-serif;color:var(--ink);background:var(--white);font-size:15px;line-height:1.6}
h1,h2,h3,h4,.nav,.btn{font-family:"Roboto",Arial,sans-serif}
section,header,footer{position:relative;width:1200px}
.section-title{font-size:30px;font-weight:500;color:var(--teal);text-align:center;letter-spacing:1px;text-transform:uppercase}
.title-rule{display:block;width:60px;height:2px;background:var(--teal);margin:14px auto 0}
.btn{display:inline-block;font-size:15px;padding:9px 22px;border:2px solid #555;color:#333;background:#fff;text-decoration:none;font-weight:500}
.btn-red{background:var(--red);border-color:var(--red);color:#fff}
.btn-light{border-color:#fff;color:#fff;background:transparent}

/* top bar */
.topbar{height:140px;display:flex;justify-content:space-between;padding:0 100px}
.brand{display:flex;align-items:center;gap:12px;margin-top:28px;height:56px}
.brand-dot{width:42px;height:42px;border-radius:50%;background:var(--teal)}
.brand-name{font-family:"Roboto",sans-serif;font-size:40px;font-weight:500;color:var(--teal)}
.topbar-right{display:flex;flex-direction:column;align-items:flex-end;gap:22px;padding-top:30px}
.contact{display:flex;gap:36px;font-size:15px;color:#555}
.contact span{display:flex;align-items:center;gap:10px}
.contact svg{width:28px;height:28px}
.nav{display:flex;gap:30px;font-size:16px;color:#333}
.nav .active{color:var(--red);border-bottom:2px solid var(--red)}

/* hero */
.hero{height:620px;overflow:hidden}
.hero-photo{position:absolute;inset:0;background:linear-gradient(100deg,#2b3b3a 0%,#51615f 40%,#3a4846 70%,#1f2b2a 100%)}
.hero-content{position:absolute;top:110px;left:0;right:0;text-align:center;color:#fff}
.hero-content h1{font-size:58px;font-weight:500;letter-spacing:1px}
.hero-content p{font-size:18px;margin:22px auto 28px;width:560px;line-height:1.5}
.hero-arrow{position:absolute;top:210px;width:40px;height:70px}
.hero-arrow.left{left:30px}.hero-arrow.right{right:30px}
.hero-curve{position:absolute;left:0;bottom:0;width:1200px;height:110px}

/* about */
.about{height:400px;padding-top:60px;text-align:center}
.about p{width:960px;margin:40px auto 40px;font-size:14px;color:var(--muted)}
.about .btn+.btn{margin-left:14px}

/* features */
.features{height:480px;background:var(--teal);color:#fff;display:flex;padding:60px 100px 0;gap:70px}
.features-text{width:400px}
.features-text h2{font-size:30px;font-weight:500;letter-spacing:1px}
.features-text h3{font-size:16px;font-weight:700;margin:30px 0 12px;text-transform:uppercase}
.features-text p{font-size:14px;line-height:1.7;margin-bottom:30px;opacity:.95}
.video{width:500px;height:330px;background:linear-gradient(135deg,#4d6d6a,#8fb0a8 50%,#355452);border:4px solid #fff;position:relative}
.video svg{position:absolute;left:205px;top:120px;width:90px;height:90px}

/* benefits */
.benefits{height:460px;background:var(--light);padding-top:70px}
.benefit-row{display:flex;justify-content:center;gap:80px;margin-top:50px}
.benefit{width:280px;text-align:center}
.benefit-icon{width:120px;height:120px;border-radius:50%;border:3px solid var(--teal);margin:0 auto;display:flex;align-items:center;justify-content:center;background:#fff}
.benefit-icon.featured{background:var(--red);border-color:var(--red);box-shadow:0 0 0 6px #fff,0 0 0 9px var(--red)}
.benefit h3{font-size:18px;font-weight:500;margin:22px 0 8px}
.benefit.featured-text h3{color:var(--red)}
.benefit p{font-size:12px;color:var(--muted);margin-bottom:14px}
.benefit .btn{font-size:12px;padding:5px 14px}

/* references */
.references{height:360px;padding-top:60px}
.ref-row{display:flex;justify-content:center;gap:50px;margin-top:60px}
.ref-badge{width:130px;height:90px;background:#f6f6f6;display:flex;align-items:center;justify-content:center}
.ref-badge span{display:block;width:80px;height:30px;background:#cfcfcf;border-radius:4px}

/* products */
.products{height:660px;background:var(--light);padding-top:70px;text-align:center}
.products .intro{font-size:14px;color:var(--muted);width:520px;margin:26px auto 0}
.product-wave{position:absolute;left:0;top:270px;width:1200px;height:120px}
.product-row{display:flex;justify-content:center;gap:60px;margin-top:40px;position:relative}
.product{width:220px}
.product-photo{width:200px;height:200px;border-radius:50%;margin:0 auto;border:6px solid var(--teal);background:radial-gradient(circle,#7fa9a3,#2f5450)}
.product-photo.featured{border-color:var(--red)}
.product h3{font-size:18px;font-weight:500;color:var(--teal);margin:14px 0 6px}
.product.featured h3{color:var(--red)}
.product p{font-size:12px;color:var(--muted);margin-bottom:12px}
.product .btn{font-size:12px;padding:5px 14px}

/* solutions */
.solutions{height:580px;padding-top:60px}
.solution-row{display:flex;justify-content:center;gap:40px;margin-top:50px}
.solution{width:300px;background:#fff;box-shadow:0 2px 8px rgba(0,0,0,.12)}
.solution-photo{height:170px;background:linear-gradient(135deg,#3e5e5b,#8db3ad 60%,#2c3d3c)}
.solution-body{padding:18px 20px 22px}
.solution h3{font-size:17px;font-weight:500;color:var(--red);margin-bottom:6px}
.solution:not(:first-child) h3{color:#333}
.solution p{font-size:12px;color:var(--muted);margin-bottom:10px}
.solution a{font-size:13px;color:#333;font-weight:600;text-decoration:none}

/* footer */
.footer{height:380px;background:var(--dark);color:#ddd;text-align:center;padding-top:40px}
.footer .brand{justify-content:center;margin:0}
.footer .brand-name{color:#fff}
.footer .brand-dot{background:#fff}
.footer .contact{justify-content:center;color:#ddd;margin-top:34px;font-size:16px}
.footer-nav{display:flex;justify-content:center;gap:26px;margin-top:40px;font-family:"Roboto",sans-serif;font-size:14px;letter-spacing:1px}
.footer-nav span{color:#777}
.footer-bottom{position:absolute;left:100px;right:100px;bottom:24px;border-top:1px solid #444;padding-top:20px;display:flex;justify-content:space-between;align-items:center;font-size:14px}
.social{display:flex;gap:10px}
.social i{display:block;width:30px;height:30px;border-radius:50%;border:1px solid #aaa}
</style>
</head>
<body>

<header class="topbar">
  <div class="brand"><span class="brand-dot"></span><span class="brand-name">Quorvia</span></div>
  <div class="topbar-right">
    <div class="contact">
      <span><svg viewBox="0 0 28 28"><circle cx="14" cy="14" r="14" fill="#4f9f96"/><path d="M10 8l3 3-2 2c1 2 2 3 4 4l2-2 3 3-2 2c-5 0-10-5-10-10z" fill="#fff"/></svg>180 555 0142</span>
      <span><svg viewBox="0 0 28 28"><circle cx="14" cy="14" r="14" fill="#c4161c"/><rect x="8" y="9" width="12" height="10" fill="none" stroke="#fff" stroke-width="1.6"/><path d="M8 9l6 5 6-5" fill="none" stroke="#fff" stroke-width="1.6"/></svg>info@quorvia.com</span>
    </div>
    <nav class="nav"><span class="active">Home</span><span>About</span><span>Features</span><span>Benefits</span><span>References</span><span>Products</span><span>Solutions</span><span>Contact</span></nav>
  </div>
</header>

<section class="hero">
  <div class="hero-photo" role="img" aria-label="Surgical team operating in a dimly lit operating room"></div>
  <div class="hero-content">
    <h1>WELCOME TO QUORVIA</h1>
    <p>A video-based teaching platform for surgical procedures, planning for your future medical needs.</p>
    <a class="btn btn-red">Read More</a>
  </div>
  <svg class="hero-arrow left" viewBox="0 0 40 70"><path d="M30 8L8 35l22 27" fill="none" stroke="#fff" stroke-width="4"/></svg>
  <svg class="hero-arrow right" viewBox="0 0 40 70"><path d="M10 8l22 27-22 27" fill="none" stroke="#fff" stroke-width="4"/></svg>
  <svg class="hero-curve" viewBox="0 0 1200 110" preserveAspectRatio="none">
    <path d="M0 30 Q600 140 1200 30 L1200 110 L0 110Z" fill="#4f9f96"/>
    <path d="M0 55 Q600 160 1200 55 L1200 110 L0 110Z" fill="#fff"/>
  </svg>
</section>

<section class="about">
  <h2 class="section-title">About the Company</h2><span class="title-rule"></span>
  <p>Quorvia is building a video based cloud teaching platform for all kinds of medical procedures using synchronised high resolution 360° and wide angle videos in a virtual reality environment. Almost daily medical device companies, doctors and surgeons all over the world develop new or breakthrough products, medical and surgical techniques. These techniques now have to increase the survival rate of more patients.</p>
  <a class="btn btn-red">Read More</a><a class="btn">Contact Us</a>
</section>

<section class="features">
  <div class="features-text">
    <h2>OUR FEATURES</h2>
    <h3>Teaching Platform</h3>
    <p>Once the surgery is captured all the info can be accessed online with the unique feature that, although the surgery is filmed in advance, the presenter has real-time full control over the imaging he wants to use. Where there is a surgeon, the presenter of the live session can experience each step of the surgery as it happens, with every angle available for teaching and review.</p>
    <a class="btn btn-light">Read More</a>
  </div>
  <div class="video" role="img" aria-label="Video still of surgeons in an operating room">
    <svg viewBox="0 0 90 90"><circle cx="45" cy="45" r="42" fill="rgba(0,0,0,.45)" stroke="#fff" stroke-width="3"/><path d="M36 28l26 17-26 17z" fill="#fff"/></svg>
  </div>
</section>

<section class="benefits">
  <h2 class="section-title">Our Company Benefits</h2><span class="title-rule"></span>
  <div class="benefit-row">
    <div class="benefit">
      <div class="benefit-icon"><svg width="56" height="56" viewBox="0 0 56 56"><circle cx="20" cy="10" r="6" fill="#4f9f96"/><path d="M12 20h16v30h-16z" fill="#4f9f96"/><circle cx="40" cy="30" r="10" fill="none" stroke="#4f9f96" stroke-width="3"/><text x="40" y="35" font-size="14" text-anchor="middle" fill="#4f9f96" font-family="Roboto">$</text></svg></div>
      <h3>More cost-effective</h3>
      <p>Medical and surgical knowledge can be shared in a faster, easier and more cost effective way than current solutions like books.</p>
      <a class="btn">Read More</a>
    </div>
    <div class="benefit featured-text">
      <div class="benefit-icon featured"><svg width="56" height="56" viewBox="0 0 56 56"><circle cx="28" cy="20" r="12" fill="none" stroke="#fff" stroke-width="3"/><path d="M22 34h12v8h-12z" fill="#fff"/><path d="M24 46h8" stroke="#fff" stroke-width="3"/></svg></div>
      <h3>Faster Sharing Of Knowledge</h3>
      <p>Medical and surgical knowledge can be shared in a faster, easier and more cost effective way than current solutions like books.</p>
      <a class="btn btn-red">Read More</a>
    </div>
    <div class="benefit">
      <div class="benefit-icon"><svg width="56" height="56" viewBox="0 0 56 56"><rect x="6" y="10" width="44" height="30" fill="none" stroke="#4f9f96" stroke-width="3"/><path d="M14 32l10-10 8 6 10-10" fill="none" stroke="#4f9f96" stroke-width="3"/><path d="M20 48h16" stroke="#4f9f96" stroke-width="3"/></svg></div>
      <h3>More Effective Learning</h3>
      <p>Medical and surgical knowledge can be shared in a faster, easier and more cost effective way than current solutions like books.</p>
      <a class="btn">Read More</a>
    </div>
  </div>
</section>

<section class="references">
  <h2 class="section-title">References</h2><span class="title-rule"></span>
  <div class="ref-row">
    <div class="ref-badge"><span></span></div><div class="ref-badge"><span></span></div><div class="ref-badge"><span></span></div>
    <div class="ref-badge"><span></span></div><div class="ref-badge"><span></span></div><div class="ref-badge"><span></span></div>
  </div>
</section>

<section class="products">
  <h2 class="section-title">Our Products</h2><span class="title-rule"></span>
  <p class="intro">Medical and surgical knowledge can be shared in a faster, easier and more cost effective way than current solutions like books.</p>
  <svg class="product-wave" viewBox="0 0 1200 120" preserveAspectRatio="none"><path d="M0 80 C200 10 300 110 500 60 S850 10 1000 70 S1150 40 1200 50" fill="none" stroke="#9cc5bf" stroke-width="3"/></svg>
  <div class="product-row">
    <div class="product"><div class="product-photo" role="img" aria-label="Surgeons performing a live procedure"></div><h3>Live</h3><p>Medical and surgical knowledge can be shared in a faster, easier and more cost effective way.</p><a class="btn">Read More</a></div>
    <div class="product featured"><div class="product-photo featured" role="img" aria-label="Surgical team recording a procedure"></div><h3>bTamo</h3><p>Medical and surgical knowledge can be shared in a faster, easier and more cost effective way.</p><a class="btn btn-red">Read More</a></div>
    <div class="product"><div class="product-photo" role="img" aria-label="Operating room with video equipment"></div><h3>bTamo local</h3><p>Medical and surgical knowledge can be shared in a faster, easier and more cost effective way.</p><a class="btn">Read More</a></div>
    <div class="product"><div class="product-photo" role="img" aria-label="Surgeons at work under theatre lights"></div><h3>bTamo cloud</h3><p>Medical and surgical knowledge can be shared in a faster, easier and more cost effective way.</p><a class="btn">Read More</a></div>
  </div>
</section>

<section class="solutions">
  <h2 class="section-title">Our Solutions</h2><span class="title-rule"></span>
  <div class="solution-row">
    <div class="solution"><div class="solution-photo" role="img" aria-label="Medical device demonstration in an operating room"></div><div class="solution-body"><h3>For Medical Device Companies</h3><p>Almost daily medical device companies, doctors and surgeons all over the world develop new or breakthrough products.</p><a>Read More &gt;&gt;</a></div></div>
    <div class="solution"><div class="solution-photo" role="img" aria-label="Doctors and surgeons during a procedure"></div><div class="solution-body"><h3>Doctor and Surgeons</h3><p>Almost daily medical device companies, doctors and surgeons all over the world develop new or breakthrough products.</p><a>Read More &gt;&gt;</a></div></div>
    <div class="solution"><div class="solution-photo" role="img" aria-label="Audience at a medical conference"></div><div class="solution-body"><h3>Medical Conferences</h3><p>Almost daily medical device companies, doctors and surgeons all over the world develop new or breakthrough products.</p><a>Read More &gt;&gt;</a></div></div>
  </div>
</section>

<footer class="footer">
  <div class="brand"><span class="brand-dot"></span><span class="brand-name">Quorvia</span></div>
  <div class="contact">
    <span><svg viewBox="0 0 28 28"><circle cx="14" cy="14" r="13" fill="none" stroke="#ddd" stroke-width="1.5"/><rect x="8" y="9" width="12" height="10" fill="none" stroke="#ddd" stroke-width="1.5"/><path d="M8 9l6 5 6-5" fill="none" stroke="#ddd" stroke-width="1.5"/></svg>info@quorvia.com</span>
    <span><svg viewBox="0 0 28 28"><circle cx="14" cy="14" r="13" fill="none" stroke="#ddd" stroke-width="1.5"/><path d="M10 8l3 3-2 2c1 2 2 3 4 4l2-2 3 3-2 2c-5 0-10-5-10-10z" fill="#ddd"/></svg>180 555 0142</span>
  </div>
  <nav class="footer-nav">HOME <span>|</span> ABOUT <span>|</span> FEATURES <span>|</span> BENEFITS <span>|</span> REFERENCES <span>|</span> PRODUCTS <span>|</span> SOLUTIONS</nav>
  <div class="footer-bottom">
    <span>© 2016 Quorvia. All Rights Reserved</span>
    <div class="social"><i></i><i></i><i></i><i></i><i></i></div>
  </div>
</footer>

</body>
</html>
```